Need a web site design for a moving company

We need to re-design our website for our moving company based in New York. Our current web site (brightcartageusa.com) is very inconvenient for our customers to navigate and finding what they are looking for. We would like a web site which can have the customers fill up the Free Moving Quote after browsing it. So we want you to be creative with overall design and a quote form. We would love to target different locations, so we want our customers to be able to switch conveniently accordingly where they are located. We have a rateloop page with testimonials, which we wanted to be there as well (not just a text, and name. Boxes with pictures, profiles, just something creative and attractive). Attached is the logo, with two options(brightcart -blue and brightcart - orange, so the colors can be used accordingly or you can use your own colors if needed (if looks the best). If surfing the inner pages, we want our customers to be able to submit a quote request if needed.

Menu:
Home Services Moving Tips Testimonials About FAQ Blog Contact Us (doesn't have to be in order)

Inner Pages:
Services, Moving Tips, Testimonials, About, FAQ, Blog (moving quote is not necessary), Contact Us

Websites as references:
fetchporters.com
holdroomly.com
calmhaulers.com
tinytruckers.com.au
cityvanline.com
finchhaulage.co.uk
shiftforus.com

Reason: We are not in rush and really need someone who can read our brief throughout. We are looking for a new web site design. It doesn't have to an updated version of our current website as most of the submitted designs are. Also not all the content from a current website should be placed into a new one (depending on a style of a new layout or design you can partially copy paste some of the content). You can be as much creative as you can, making it clean looking, flat color with attractive user interface. If a menu is too long, we can skip some of them and place them in footer. The main things we are concerned about are quote form, option of location look up (switch between locations) and reviews (at least some part of the page should be dedicated to it). If you have any questions or if our brief is not clear, please let us know about it, Thank you

Industry/Entity Type

Moving Company

```html
<!DOCTYPE html>
<html lang="en">
<head>
<meta charset="utf-8">
<title>Brightcart Movers – Moving Company Based In New York</title>
<link rel="stylesheet" href="https://fonts.googleapis.com/css2?family=Cabin:wght@400;500;600;700&family=Open+Sans:wght@300;400;600;700&display=swap">
<style>
:root{
  --red:#e94759;
  --blue:#1d5aa6;
  --blue-dark:#12427e;
  --navy:#1c2b48;
  --ink:#222;
  --grey:#666;
  --light:#f4f4f4;
  --footer:#343434;
  --white:#fff;
}
*{box-sizing:border-box;margin:0;padding:0}
html,body{width:1200px;height:2496px;overflow:hidden}
body{font-family:"Open Sans",Arial,sans-serif;color:var(--ink);background:var(--white);position:relative}
section,header,footer,nav{position:relative;width:1200px}
.abs{position:absolute}

/* hero */
.hero{height:552px;border-top:8px solid var(--blue);overflow:hidden}
.hero-photo{position:absolute;inset:0;background:linear-gradient(100deg,#b89a72 0%,#d9c3a2 30%,#e8dccb 55%,#c9a57b 80%,#a07c55 100%)}
.hero-title{position:absolute;left:90px;top:236px;width:580px;text-align:center;color:var(--white);font-family:"Cabin",sans-serif;font-weight:600;font-size:39px;line-height:42px;text-shadow:0 2px 4px rgba(0,0,0,.5)}
.slide-arrow{position:absolute;top:238px;width:74px;height:74px;background:rgba(60,60,60,.75);display:flex;align-items:center;justify-content:center}
.slide-arrow.prev{left:0}.slide-arrow.next{right:0}
.quote-form{position:absolute;left:842px;top:44px;width:260px;height:426px;background:rgba(245,232,205,.92)}
.quote-form h2{position:absolute;left:-14px;top:0;width:274px;height:42px;background:var(--red);color:var(--white);font-family:"Cabin",sans-serif;font-weight:500;font-size:22px;line-height:42px;text-align:center}
.quote-field{position:absolute;left:14px;width:232px;height:34px;background:var(--white);border:1px solid #d8cdb8;font-size:13px;color:#555;padding-left:10px;line-height:32px}
.quote-field::after{content:"*";position:absolute;right:8px;top:1px;color:var(--red)}
.quote-type{position:absolute;top:334px;font-size:14px;color:#333;display:flex;align-items:center;gap:10px}
.quote-type i{display:inline-block;width:20px;height:20px;background:var(--white);border:1px solid #999}
.quote-type i.on{background:#8a8a8a}
.quote-submit{position:absolute;left:154px;top:376px;width:92px;height:36px;background:var(--red);color:var(--white);font-size:13px;line-height:36px;text-align:center}

/* nav */
.site-nav{height:128px;border-top:10px solid var(--blue);border-bottom:8px solid var(--blue);background:var(--white)}
.brand{position:absolute;left:94px;top:30px;display:flex;align-items:center;gap:10px;font-family:"Cabin",sans-serif;font-weight:700;font-size:18px;color:var(--red);letter-spacing:.5px}
.brand i{display:block;width:34px;height:34px;background:var(--blue)}
.menu{position:absolute;left:418px;top:0;height:110px;display:flex;list-style:none}
.menu li{font-family:"Cabin",sans-serif;font-size:17px;color:#222;line-height:110px;padding:0 10px}
.menu li.current{background:var(--red);color:var(--white);padding:0 18px}

/* welcome */
.welcome{height:134px;text-align:center}
.welcome h1{position:absolute;top:42px;width:100%;font-family:"Cabin",sans-serif;font-weight:700;font-size:29px;color:var(--ink)}
.welcome h1 span{color:var(--red)}
.welcome p{position:absolute;top:82px;width:100%;font-family:"Cabin",sans-serif;font-size:40px;color:var(--ink)}

/* services */
.services{height:409px;background:var(--red)}
.service{position:absolute;top:37px;width:240px;height:339px;text-align:center;color:var(--white)}
.service.featured{background:var(--blue)}
.service h3{position:absolute;top:22px;width:100%;font-family:"Cabin",sans-serif;font-weight:500;font-size:20px;line-height:24px}
.service svg{position:absolute;left:60px;top:80px}
.service p{position:absolute;top:200px;left:26px;width:188px;font-size:11.5px;line-height:15px;font-weight:600}
.btn-more{position:absolute;left:77px;top:278px;width:86px;height:36px;border:2px solid var(--white);font-size:12px;font-weight:700;line-height:32px}

/* newsletter */
.newsletter{height:156px;background:linear-gradient(90deg,#254d86 0%,#3c6aa8 45%,#4b78b0 70%,#2a5590 100%)}
.newsletter h2{position:absolute;left:172px;top:58px;color:var(--white);font-weight:300;font-size:28px}
.newsletter p{position:absolute;left:500px;top:52px;width:290px;color:var(--white);font-size:13.5px;line-height:17px;font-weight:700}
.news-input{position:absolute;left:778px;top:71px;width:218px;height:30px;background:#eee;color:#999;font-size:13px;line-height:30px;padding-left:10px}
.news-btn{position:absolute;left:996px;top:71px;width:88px;height:30px;background:var(--blue);color:var(--white);font-size:13px;line-height:30px;text-align:center}

/* tips */
.tips{height:323px;background:var(--light)}
.tip{position:absolute;top:72px;width:300px;text-align:center}
.tip h3{font-family:"Cabin",sans-serif;font-weight:700;font-size:21px;color:var(--navy)}
.tip hr{width:80px;margin:6px auto 0;border:0;border-top:3px solid var(--blue)}
.tip p{margin-top:14px;font-size:12.5px;line-height:17px;color:var(--grey)}
.tip .btn-tip{display:inline-block;margin-top:26px;width:72px;height:34px;border:2px solid #6a8fc0;background:var(--white);color:#333;font-size:13px;line-height:30px}

/* testimonials */
.testimonials{height:395px;background:linear-gradient(180deg,#3f6eab 0%,#5a85bb 50%,#2f5d96 100%)}
.testimonials h2{position:absolute;top:56px;width:100%;text-align:center;color:var(--white);font-weight:300;font-size:40px;letter-spacing:1px}
.testimonials hr{position:absolute;left:292px;top:124px;width:614px;border:0;border-top:2px solid #6fa0e0}
.testimonials blockquote{position:absolute;left:280px;top:164px;width:640px;text-align:center;color:var(--white);font-size:16px;line-height:26px}
.avatar{position:absolute;left:547px;top:226px;width:92px;height:92px;border-radius:50%;background:#d8d8d8;border:4px solid var(--white)}
.testimonials cite{position:absolute;top:332px;width:100%;text-align:center;color:var(--white);font-style:normal;font-size:16px}
.t-arrow{position:absolute;top:196px}

/* footer */
.site-footer{height:357px;background:var(--footer);color:#ddd}
.site-footer h4{position:absolute;font-family:"Cabin",sans-serif;font-weight:500;font-size:18px;color:var(--white)}
.social{position:absolute;left:108px;top:80px;display:flex;gap:12px}
.social i{display:block;width:38px;height:38px;border-radius:50%;background:#5a5a5a}
.social i:first-child{background:var(--blue)}
.post{position:absolute;left:108px;top:196px;width:270px;font-size:12.5px;line-height:18px}
.post .date{color:var(--blue);font-size:11px}
.post .read{color:var(--blue);font-size:11px;margin-top:4px}
.ad-list{position:absolute;left:443px;top:84px;width:276px;list-style:none}
.ad-list li{height:25px;border-bottom:1px solid #888;font-size:10.5px;line-height:24px;color:#ddd;padding-left:2px}
.ad-list li::before{content:"› ";color:#999}
.contact-field{position:absolute;left:815px;width:275px;background:#ddd;color:#777;font-family:Georgia,serif;font-size:12px;padding:6px 8px}
.contact-submit{position:absolute;left:1019px;top:301px;width:71px;height:26px;background:var(--blue);color:var(--white);font-size:11px;font-weight:700;line-height:26px;text-align:center}
.bottom-bar{position:absolute;left:0;top:2462px;width:1200px;height:34px;border-top:4px solid var(--red);background:var(--blue)}
</style>
</head>
<body>

<header class="hero">
  <div class="hero-photo" role="img" aria-label="Smiling couple sitting on the floor among moving boxes in a bright new home"></div>
  <p class="hero-title">WHEN YOU MOVE WITH US,<br>IT'S ALMOST FUN</p>
  <div class="slide-arrow prev"><svg width="20" height="32" viewBox="0 0 20 32"><path d="M16 3 4 16l12 13" fill="none" stroke="#fff" stroke-width="4"/></svg></div>
  <div class="slide-arrow next"><svg width="20" height="32" viewBox="0 0 20 32"><path d="M4 3l12 13L4 29" fill="none" stroke="#fff" stroke-width="4"/></svg></div>
  <form class="quote-form">
    <h2>GET A FREE QUOTE NOW</h2>
    <div class="quote-field" style="top:70px">Name</div>
    <div class="quote-field" style="top:114px">Phone #</div>
    <div class="quote-field" style="top:158px">Email</div>
    <div class="quote-field" style="top:202px">Move From</div>
    <div class="quote-field" style="top:246px">Move To</div>
    <div class="quote-field" style="top:290px">Date</div>
    <div class="quote-type" style="left:14px"><i class="on"></i>Residential</div>
    <div class="quote-type" style="left:128px"><i></i>Commercial</div>
    <div class="quote-submit">Submit</div>
  </form>
</header>

<nav class="site-nav">
  <div class="brand"><i></i>BRIGHTCART MOVERS</div>
  <ul class="menu">
    <li class="current">Home</li><li>Services</li><li>Moving Tips</li><li>Testimonials</li><li>About</li><li>FAQ</li><li>Blog</li><li>Contact Us</li>
  </ul>
</nav>

<section class="welcome">
  <h1>Welcome To <span>Brightcart</span> Movers</h1>
  <p>Moving Company Based In New York</p>
</section>

<section class="services">
  <div class="service" style="left:96px">
    <h3>Residential Moving</h3>
    <svg width="120" height="100" viewBox="0 0 120 100" fill="#fff"><rect x="20" y="20" width="60" height="50" rx="4"/><path d="M82 34h18l14 18v18H82z"/><circle cx="42" cy="78" r="10" stroke="var(--red)" stroke-width="4"/><circle cx="98" cy="78" r="10" stroke="var(--red)" stroke-width="4"/><rect x="0" y="30" width="16" height="4"/><rect x="4" y="44" width="12" height="4"/><rect x="8" y="58" width="8" height="4"/></svg>
    <p>Sorrupti quos dolores et quas molestias excepturi sint occa- ecati cupiditate deserunt mollitia animi,</p>
    <div class="btn-more">More</div>
  </div>
  <div class="service" style="left:350px">
    <h3>Commercial Moving</h3>
    <svg width="120" height="100" viewBox="0 0 120 100" fill="#fff"><rect x="6" y="12" width="34" height="24"/><rect x="44" y="12" width="34" height="24"/><rect x="6" y="40" width="72" height="28"/><path d="M82 34h18l14 18v16H82z"/><circle cx="30" cy="78" r="10" stroke="var(--red)" stroke-width="4"/><circle cx="98" cy="78" r="10" stroke="var(--red)" stroke-width="4"/></svg>
    <p>Sorrupti quos dolores et quas molestias excepturi sint occa- ecati cupiditate deserunt mollitia animi,</p>
    <div class="btn-more">More</div>
  </div>
  <div class="service featured" style="left:605px">
    <h3>Interstate/Long<br>Distance Moves</h3>
    <svg width="120" height="100" viewBox="0 0 120 100"><circle cx="60" cy="52" r="40" fill="#fff"/><path d="M30 40q14-10 28 0t26 4M34 66q20-8 44 2" fill="none" stroke="var(--blue)" stroke-width="6"/><path d="M20 22l60 20" stroke="#fff" stroke-width="6"/></svg>
    <p>Sorrupti quos dolores et quas molestias excepturi sint occa- ecati cupiditate deserunt mollitia animi,</p>
    <div class="btn-more">More</div>
  </div>
  <div class="service" style="left:858px">
    <h3>Moving Supplies</h3>
    <svg width="120" height="100" viewBox="0 0 120 100" fill="none" stroke="#fff" stroke-width="5"><path d="M36 6l10 6 26 70"/><rect x="52" y="26" width="34" height="34" transform="rotate(-20 69 43)" fill="#fff"/><circle cx="76" cy="86" r="8"/><path d="M84 84l22-8"/></svg>
    <p>Sorrupti quos dolores et quas molestias excepturi sint occa- ecati cupiditate deserunt mollitia animi,</p>
    <div class="btn-more">More</div>
  </div>
</section>

<section class="newsletter" role="img" aria-label="Family carrying moving boxes under a blue tint">
  <svg class="abs" style="left:110px;top:52px" width="46" height="46" viewBox="0 0 46 46" fill="none" stroke="#fff" stroke-width="2.5"><path d="M43 3 3 20l14 6 4 16 7-10 10 7z"/><path d="M17 26 43 3"/></svg>
  <h2>Subscribe To Newsletter</h2>
  <p>Lorem ipsum dolor sit amet, consectetur adipisicing elit, sed do eiusmod tempor incididunt ut labore</p>
  <div class="news-input">Email</div>
  <div class="news-btn">Submit</div>
</section>

<section class="tips">
  <article class="tip" style="left:110px">
    <h3>Money Saving Ideas</h3><hr>
    <p>Lorem ipsum dolor sit amet, consectetur adipisicing elit, sed do eiusmod tempor incididunt ut labore et dolore magna aliqua. Ut enim ad minim veniam, quis nostrud exercitaullamco.</p>
    <span class="btn-tip">more</span>
  </article>
  <article class="tip" style="left:453px">
    <h3>Budgeting Tips</h3><hr>
    <p>Lorem ipsum dolor sit amet, consectetur adipisicing elit, sed do eiusmod tempor incididunt ut labore et dolore magna aliqua. Ut enim ad minim veniam, quis nostrud exercitaullamco.</p>
    <span class="btn-tip">more</span>
  </article>
  <article class="tip" style="left:796px">
    <h3>Time Saving Tips</h3><hr>
    <p>Lorem ipsum dolor sit amet, consectetur adipisicing elit, sed do eiusmod tempor incididunt ut labore et dolore magna aliqua. Ut enim ad minim veniam, quis nostrud exercitaullamco.</p>
    <span class="btn-tip">more</span>
  </article>
</section>

<section class="testimonials" role="img" aria-label="Children carrying cardboard boxes outdoors under a blue tint">
  <h2>TESTMONIALS</h2>
  <hr>
  <blockquote>Aenean placerat nunc lorem, vitae suscipit mi luctus quis. In ligula lorem, ultricies volutpat arcu et, ultrices cursus enim.</blockquote>
  <svg class="t-arrow" style="left:176px" width="16" height="28" viewBox="0 0 16 28"><path d="M13 2 3 14l10 12" fill="none" stroke="#fff" stroke-width="2.5"/></svg>
  <svg class="t-arrow" style="left:1008px" width="16" height="28" viewBox="0 0 16 28"><path d="M3 2l10 12L3 26" fill="none" stroke="#fff" stroke-width="2.5"/></svg>
  <div class="avatar" role="img" aria-label="Customer profile photo"></div>
  <cite>Daniel Brooks</cite>
</section>

<footer class="site-footer">
  <h4 style="left:108px;top:46px">SOCIAL LINKS</h4>
  <div class="social"><i></i><i></i><i></i></div>
  <h4 style="left:108px;top:160px">BLOGS</h4>
  <div class="post">
    <div style="color:#fff;font-size:13px;margin-bottom:6px">Post Title</div>
    <div class="date">March 12, 2015</div>
    <p>Lorem ipsum dolor sit amet, consectetur adipiscing elit. Nunc non diam erat. In fringilla massa ut nisi ullamcorper pellentesque.</p>
    <div class="read">Read More »</div>
  </div>
  <h4 style="left:443px;top:46px">ADVERTISE WITH US</h4>
  <ul class="ad-list">
    <li>Lorem ipsum dolor sit</li><li>Amet consectetur</li><li>Praesent vel sem id</li><li>Curabitur hendrerit est</li><li>Aliquam eget erat nec sapien</li><li>Cras id augue nunc</li><li>In nec justo non</li><li>Vivamus mollis enim ut</li><li>Curabitur hendrerit est</li>
  </ul>
  <h4 style="left:815px;top:46px">CONTACT US</h4>
  <div class="contact-field" style="top:79px;height:30px">Name</div>
  <div class="contact-field" style="top:116px;height:30px">Email</div>
  <div class="contact-field" style="top:158px;height:112px">Message</div>
  <div class="contact-submit">SUBMIT</div>
</footer>
<div class="bottom-bar"></div>

</body>
</html>
```